R.K. custom tile,stone,&flooring experts in unique&unusual designs with an innovative twist

we are in innovative and unique tile company specializing in custom designs our thought was a caveman chiseling a square instead of a wheel we want it to be fun but manly also want the card to stand out we are licenced and insured with over 35 years experience between the 2 of us it is a tile stone and flooring company with lots of experience in crazy design like color to be on the caveman and the square to be a piece of tile

Target Market(s)

people with money

Industry/Entity Type

Flooring

Contact Information for Business Card

owners dale minter 757 314-2297 ronnie vask 757 286-9031 14 Fernmoor rd. Newport news va. 23917

Font styles to use
Serif

Requirements
Must have
• a cool caveman with lots of detail.
Nice to have
• I would like the tile to look like a natural stone must have name of co. and the hook that comes after the name and the caveman he is important
Should not have
• anything pink we are men

```html
<!DOCTYPE html>
<html lang="en">
<head>
<meta charset="utf-8">
<title>Tile Company Business Cards</title>
<link rel="stylesheet" href="https://fonts.googleapis.com/css2?family=Archivo+Black&family=Arimo:wght@400;700&display=swap">
<style>
  :root {
    --backdrop: #8f9598;
    --card: #ffffff;
    --red: #e3100f;
    --red-deep: #b30a0a;
    --ink-dark: #2b2b2b;
    --ink-mid: #4a4a4a;
    --rule-orange: #f0a020;
    --phone-brown: #9a5a22;
    --stone: #dcdcd9;
    --stone-edge: #9b9b98;
    --fur: #f39a1d;
    --fur-light: #f8c070;
  }
  html, body {
    margin: 0;
    width: 1200px;
    height: 900px;
    overflow: hidden;
    background: var(--backdrop);
  }
  .canvas {
    position: relative;
    width: 1200px;
    height: 900px;
  }
  .card {
    position: absolute;
    width: 660px;
    height: 370px;
    background: var(--card);
    overflow: hidden;
    box-shadow: 0 6px 18px rgba(0,0,0,0.25);
  }
  .card--front { left: 230px; top: 45px; }
  .card--back  { left: 305px; top: 460px; }
  .card__swoosh {
    position: absolute;
    inset: 0;
    width: 660px;
    height: 370px;
  }
  .company-name {
    position: absolute;
    left: 0;
    width: 730px;
    top: 62px;
    margin: 0;
    text-align: center;
    font-family: "Archivo Black", sans-serif;
    font-size: 41px;
    letter-spacing: -1.5px;
    color: var(--ink-dark);
    line-height: 1;
  }
  .company-rule {
    position: absolute;
    left: 143px;
    top: 114px;
    width: 448px;
    height: 3px;
    background: var(--rule-orange);
  }
  .company-tagline {
    position: absolute;
    left: 210px;
    top: 128px;
    margin: 0;
    font-family: "Arimo", sans-serif;
    font-weight: 700;
    font-size: 36px;
    letter-spacing: 3px;
    color: var(--ink-dark);
    line-height: 1;
  }
  .mascot {
    position: absolute;
    border-radius: 18px;
    background: linear-gradient(180deg, var(--fur-light) 0%, var(--fur) 55%, #e8892a 100%);
  }
  .card--front .mascot { left: 100px; top: 176px; width: 124px; height: 176px; }
  .card--back .mascot  { left: 50px; top: 28px; width: 165px; height: 268px; }
  .stone-sign {
    position: absolute;
    background: var(--stone);
    border: 2px solid var(--stone-edge);
    border-radius: 10px;
    display: flex;
    flex-direction: column;
    justify-content: center;
    align-items: center;
    font-family: "Arimo", sans-serif;
    font-weight: 700;
    color: var(--red);
    line-height: 0.95;
    letter-spacing: -0.5px;
  }
  .card--front .stone-sign { left: 228px; top: 220px; width: 124px; height: 88px; }
  .card--back .stone-sign  { left: 222px; top: 135px; width: 150px; height: 122px; }
  .stone-sign__over { font-size: 28px; }
  .stone-sign__years { font-size: 19px; }
  .stone-sign__exp { font-size: 10px; }
  .card--back .stone-sign__over { font-size: 33px; }
  .card--back .stone-sign__years { font-size: 22px; }
  .card--back .stone-sign__exp { font-size: 12px; }
  .contacts {
    position: absolute;
    left: 403px;
    top: 48px;
    font-family: "Arimo", sans-serif;
  }
  .owner { margin: 0 0 14px; }
  .owner__name {
    margin: 0;
    font-weight: 700;
    font-size: 28px;
    letter-spacing: -0.5px;
    color: var(--ink-mid);
    line-height: 1.1;
  }
  .owner__phone {
    margin: 6px 0 0 50px;
    display: flex;
    align-items: center;
    gap: 12px;
    font-size: 17px;
    color: var(--phone-brown);
  }
  .owner__phone svg { width: 17px; height: 17px; }
  .address {
    margin: 10px 0 0 2px;
    font-size: 13px;
    line-height: 1.4;
    color: #111;
  }
</style>
</head>
<body>
<div class="canvas">

  <section class="card card--front">
    <svg class="card__swoosh" viewBox="0 0 660 370" aria-hidden="true">
      <defs>
        <linearGradient id="redFront" x1="0" y1="0" x2="1" y2="1">
          <stop offset="0" stop-color="#ff2a1e"/>
          <stop offset="1" stop-color="#c80b0b"/>
        </linearGradient>
      </defs>
      <path d="M0 0 H150 C70 20 20 70 0 150 Z" fill="url(#redFront)"/>
      <path d="M660 140 C630 250 540 330 400 370 H660 Z" fill="url(#redFront)"/>
      <path d="M660 175 C620 270 540 335 440 370" stroke="var(--red-deep)" stroke-width="2" fill="none"/>
    </svg>
    <h1 class="company-name">NAME OF COMPANY</h1>
    <div class="company-rule"></div>
    <p class="company-tagline">TILE COMPANY</p>
    <div class="mascot" role="img" aria-label="Cartoon caveman mascot in a spotted fur tunic holding a stone chisel"></div>
    <div class="stone-sign">
      <span class="stone-sign__over">OVER</span>
      <span class="stone-sign__years">35 YEARS</span>
      <span class="stone-sign__exp">OF EXPERIENCE</span>
    </div>
  </section>

  <section class="card card--back">
    <svg class="card__swoosh" viewBox="0 0 660 370" aria-hidden="true">
      <defs>
        <linearGradient id="redBack" x1="0" y1="0" x2="1" y2="1">
          <stop offset="0" stop-color="#ff2a1e"/>
          <stop offset="1" stop-color="#c80b0b"/>
        </linearGradient>
      </defs>
      <path d="M0 0 H170 C80 30 20 110 0 250 Z" fill="url(#redBack)"/>
      <path d="M660 160 C625 270 540 340 420 370 H660 Z" fill="url(#redBack)"/>
      <path d="M660 195 C620 285 545 345 460 370" stroke="var(--red-deep)" stroke-width="2" fill="none"/>
    </svg>
    <div class="mascot" role="img" aria-label="Cartoon caveman mascot in a spotted fur tunic holding a stone chisel"></div>
    <div class="stone-sign">
      <span class="stone-sign__over">OVER</span>
      <span class="stone-sign__years">35 YEARS</span>
      <span class="stone-sign__exp">OF EXPERIENCE</span>
    </div>
    <div class="contacts">
      <div class="owner">
        <p class="owner__name">Dale Minter</p>
        <p class="owner__phone">
          <svg viewBox="0 0 20 20" aria-hidden="true"><circle cx="10" cy="10" r="10" fill="#333"/><path d="M7 5 L8.6 5.3 L9.2 7.6 L8 8.5 C8.6 10 9.9 11.4 11.5 12 L12.4 10.8 L14.7 11.4 L15 13 C13.5 15 10 14.5 7.5 12 C5.2 9.6 5 6.5 7 5 Z" fill="#fff"/></svg>
          757 314-2297
        </p>
      </div>
      <div class="owner">
        <p class="owner__name">Ronnie Vask</p>
        <p class="owner__phone">
          <svg viewBox="0 0 20 20" aria-hidden="true"><circle cx="10" cy="10" r="10" fill="#333"/><path d="M7 5 L8.6 5.3 L9.2 7.6 L8 8.5 C8.6 10 9.9 11.4 11.5 12 L12.4 10.8 L14.7 11.4 L15 13 C13.5 15 10 14.5 7.5 12 C5.2 9.6 5 6.5 7 5 Z" fill="#fff"/></svg>
          757 286-9031
        </p>
      </div>
      <p class="address">14 Fernmoor Rd.<br>Newport News Va. 23917</p>
    </div>
  </section>

</div>
</body>
</html>
```